Paper Lantern Theory - Podcast Cover

Paper Lantern Theory is a weekly podcast that dispels some of the myths about conventional economic thinking and provides a new way of thinking about issues that are faced by the global economy. It's insightful, thought-provoking and, most importantly, fun. We are refreshing the look and sound of the podcast. I have attached a copy of the old amateur design (which I did!)

Target Market(s)

Male oriented, smart folk with an interest in politics and economics

Font styles to use
Sans Serif

Requirements
Must have
• Clearly visible title, even when reduced in size. Must be 3000 pixels by 3000 pixels.
Nice to have
• This podcast challenges the status quo. It should reflect that. Photos and names of the hosts. Actually, because th ephotos are so different, we'd be open to the idea of a caricature if you can do that within the price.

```html
<!DOCTYPE html>
<html lang="en">
<head>
<meta charset="UTF-8">
<title>Paper Lantern Theory – Podcast Cover</title>
<link rel="stylesheet" href="https://fonts.googleapis.com/css2?family=Bungee&family=Montserrat:wght@700&display=swap">
<style>
  :root {
    --teal-deep: #033b45;
    --teal-pattern: #0b4a52;
    --white: #ffffff;
    --host-left: #cdbfb2;
    --host-left-shade: #a99a8d;
    --host-right: #3f93aa;
    --host-right-shade: #2c7288;
  }
  html, body {
    margin: 0;
    padding: 0;
    width: 1200px;
    height: 1200px;
    overflow: hidden;
    background: var(--teal-deep);
  }
  .cover {
    position: relative;
    width: 1200px;
    height: 1200px;
    background: var(--teal-deep);
    overflow: hidden;
  }
  .cover-art { position: absolute; inset: 0; }
  .pattern-field { fill: var(--teal-deep); }
  .frame-line { fill: none; stroke: var(--white); stroke-width: 2.5; }
  .mic-icon { fill: none; stroke: var(--white); stroke-width: 3; stroke-linecap: round; }
  .kicker {
    font-family: 'Montserrat', sans-serif;
    font-weight: 700;
    font-size: 32px;
    letter-spacing: 12px;
    fill: var(--white);
  }
  .show-title {
    font-family: 'Bungee', sans-serif;
    fill: var(--white);
  }
  .host-left { fill: url(#hostLeftTone); }
  .host-right { fill: url(#hostRightTone); }
</style>
</head>
<body>
<main class="cover">
  <svg class="cover-art" width="1200" height="1200" viewBox="0 0 1200 1200" xmlns="http://www.w3.org/2000/svg">
    <defs>
      <linearGradient id="hostLeftTone" x1="0" y1="0" x2="0" y2="1">
        <stop offset="0" stop-color="var(--host-left-shade)"/>
        <stop offset="1" stop-color="var(--host-left)"/>
      </linearGradient>
      <linearGradient id="hostRightTone" x1="0" y1="0" x2="0" y2="1">
        <stop offset="0" stop-color="var(--host-right-shade)"/>
        <stop offset="1" stop-color="var(--host-right)"/>
      </linearGradient>
    </defs>

    <rect class="pattern-field" x="0" y="0" width="1200" height="1200"
          role="img" aria-label="Faint pattern of banknotes scattered across the dark teal background"/>

    <rect class="frame-line" x="41" y="42" width="1118" height="1180"/>

    <g class="mic-icon" transform="translate(600 118)">
      <rect x="-9" y="-32" width="18" height="34" rx="9"/>
      <path d="M-17 -6 v4 a17 17 0 0 0 34 0 v-4"/>
      <line x1="0" y1="15" x2="0" y2="31"/>
    </g>

    <text class="kicker" x="606" y="186" text-anchor="middle">PODCAST</text>

    <text class="show-title" x="118" y="388" font-size="206"
          textLength="966" lengthAdjust="spacingAndGlyphs">PAPER LANTERN</text>
    <text class="show-title" x="118" y="566" font-size="206"
          textLength="966" lengthAdjust="spacingAndGlyphs">THEORY</text>

    <path class="host-left" role="img" aria-label="Photo of the first host in a white T-shirt"
          d="M22 1200 L40 1010 Q80 960 220 935 L230 760 Q240 640 340 625 Q440 615 450 760 L445 935 Q540 960 562 1010 L562 1200 Z"/>

    <path class="host-right" role="img" aria-label="Photo of the second host, smiling, in a blue polo shirt"
          d="M528 1200 L560 1010 Q600 950 760 925 L755 770 Q765 645 855 640 Q960 640 975 775 L965 925 Q1130 950 1180 1040 L1200 1200 Z"/>
  </svg>
</main>
</body>
</html>
```